Velvet Orchard - R&B Band in Sydney Requires new Business Cards

We're a 6 piece R&B Soul band in Sydney called Velvet Orchard that requires new promotional material including Business Cards.

We are very well known around Sydney and have a resident venue gig at the Marlowe Sydney hotel. We play predominantly old & new school R&B hits.

Our logo is attached, colours are Brown & yellow.
Initial idea was to get sugar packets made up with our logo and contact details.

```html
<!DOCTYPE html>
<html lang="en">
<head>
<meta charset="utf-8">
<title>Velvet Orchard – Business Cards</title>
<link rel="stylesheet" href="https://fonts.googleapis.com/css2?family=Arimo:wght@400;700&display=swap">
<style>
  :root {
    --backdrop: #ebebeb;
    --sugar-yellow: #ffee00;
    --sugar-yellow-light: #fff45a;
    --cocoa: #3b2512;
    --cocoa-light: #5a412c;
    --mic-brown: #7a5a1e;
    --mic-tan: #b8974a;
    --ink: #2b2b2b;
    --ink-soft: #6a6a3a;
    --card-w: 520px;
    --card-h: 297px;
  }
  * { box-sizing: border-box; margin: 0; padding: 0; }
  html, body {
    width: 1200px; height: 900px; overflow: hidden;
    background: var(--backdrop);
    font-family: "Arimo", Arial, sans-serif;
  }
  .stage {
    width: 1200px; height: 900px;
    display: flex; align-items: center; justify-content: center; gap: 44px;
  }
  .card {
    width: var(--card-w); height: var(--card-h);
    position: relative; overflow: hidden;
    box-shadow: 0 10px 24px rgba(0,0,0,0.18);
  }
  /* Front: contact side */
  .card--front {
    background: linear-gradient(160deg, var(--sugar-yellow-light) 0%, var(--sugar-yellow) 55%);
  }
  .mic-art {
    position: absolute; left: 0; top: 0; width: 150px; height: 100%;
    background: linear-gradient(90deg, var(--mic-brown) 0%, var(--mic-tan) 70%, rgba(184,151,74,0) 100%);
    opacity: 0.85;
  }
  .contact {
    position: absolute; left: 170px; top: 30px; right: 20px;
    color: var(--ink);
  }
  .contact__name { font-size: 20px; font-weight: 400; color: var(--ink-soft); }
  .contact__role,
  .contact__company { font-size: 14px; color: var(--ink-soft); line-height: 1.35; }
  .contact__role { margin-top: 4px; }
  .contact__details { margin-top: 12px; list-style: none; }
  .contact__details li { font-size: 15px; line-height: 1.35; color: var(--ink-soft); }
  .contact__details li.contact__web { color: var(--ink); }
  .social { list-style: none; margin-top: 2px; }
  .social li {
    display: flex; align-items: center; gap: 7px;
    font-size: 15px; line-height: 1.38; color: var(--ink);
  }
  .social__mark {
    width: 11px; height: 11px; background: var(--ink); flex: none;
  }
  /* Back: name side */
  .card--back {
    background: linear-gradient(165deg, var(--cocoa-light) 0%, var(--cocoa) 45%);
    display: flex; align-items: center; justify-content: center;
  }
  .brand-name {
    color: var(--sugar-yellow);
    font-family: "Arimo", Arial, sans-serif;
    font-weight: 700; font-size: 46px; letter-spacing: 2px;
    text-transform: uppercase; text-align: center; line-height: 1.05;
  }
</style>
</head>
<body>
<main class="stage">
  <section class="card card--front">
    <div class="mic-art" role="img" aria-label="Large vintage microphone illustration in brown tones"></div>
    <div class="contact">
      <p class="contact__name">Rena Castellano</p>
      <p class="contact__role">Director</p>
      <p class="contact__company">Velvet Orchard Entertainment Pty Ltd</p>
      <ul class="contact__details">
        <li>+61 412 300 725</li>
        <li>info@velvetorchardmusic.com.au</li>
        <li class="contact__web">www.velvetorchardmusic.com.au</li>
      </ul>
      <ul class="social">
        <li><span class="social__mark"></span>www.facebook.com/velvetorchardent</li>
        <li><span class="social__mark"></span>twitter.com/velvet_orchard_ent</li>
        <li><span class="social__mark"></span>www.youtube.com/velvetorchardsyd</li>
        <li><span class="social__mark"></span>instagram.com/velvetorchardmusic</li>
      </ul>
    </div>
  </section>
  <section class="card card--back">
    <p class="brand-name">Velvet<br>Orchard</p>
  </section>
</main>
</body>
</html>
```